Bref créative
Bright Path Fund - Not for Profit - Stationary and Business Cards
Professional
Dale Meridew
President and Chairman of the Board
20573 Lindale Avenue #238
Helotes, Texas 78154
dale.meridew@brightpathfund.org
www.brightpathfund.org
Implement colors from the logo theme.
incorporate the logo into the design.
Bright Path Fund logo - AI format

```html
<!DOCTYPE html>
<html lang="en">
<head>
<meta charset="utf-8">
<title>Bright Path Fund Stationery</title>
<link href="https://fonts.googleapis.com/css2?family=Montserrat:wght@700;800&family=Open+Sans:wght@400;600&display=swap" rel="stylesheet">
<style>
:root{
  --red:#e31e24;
  --ink:#333333;
  --muted:#8a8a8a;
  --rule:#c9c9c9;
  --paper:#ffffff;
  --stage:#222222;
  --card-dark:#2b2b2b;
  --band-grey:#dddddd;
}
*{box-sizing:border-box;margin:0;padding:0}
html,body{width:1200px;height:569px;overflow:hidden;background:var(--stage)}
body{position:relative;font-family:"Open Sans",Arial,sans-serif;color:var(--ink)}
.sheet{position:absolute;background:var(--paper);overflow:hidden;box-shadow:0 2px 8px rgba(0,0,0,.5)}
.swoosh{position:absolute;left:0;bottom:0;width:100%}
.brand{display:flex;align-items:center;gap:5px;font-family:"Montserrat",Arial,sans-serif;font-weight:800;color:var(--red);line-height:1}
.brand-name{display:block}
.brand.stacked .brand-name{white-space:normal}
.brand.single .brand-name{white-space:nowrap}
.brand-dot{border-radius:50%;background:var(--red);flex:none}
.brand.on-red,.brand.on-dark{color:var(--paper)}
.brand.on-red .brand-dot,.brand.on-dark .brand-dot{background:var(--paper)}
.contact{position:absolute;font-size:5px;line-height:7.5px;color:var(--muted);white-space:nowrap}
.contact b{color:var(--red);font-weight:600}

.letterhead{left:36px;top:60px;width:300px;height:480px}
.fax{left:360px;top:60px;width:300px;height:480px}
.letterhead .brand,.fax .brand{position:absolute;left:16px;top:20px;font-size:16px}
.letterhead .brand-name,.fax .brand-name{width:112px}
.letterhead .brand-dot,.fax .brand-dot{width:18px;height:18px}
.letterhead .contact,.fax .contact{left:182px;top:20px}
.fax-title{position:absolute;left:18px;top:84px;font-family:"Montserrat",Arial,sans-serif;font-weight:700;font-size:20px;letter-spacing:1px;color:var(--ink)}
.fax-fields{position:absolute;left:18px;top:126px;width:264px;display:grid;grid-template-columns:1fr 1fr;column-gap:16px;row-gap:12px}
.field{display:flex;align-items:flex-end;gap:4px;font-size:5.5px;color:var(--ink)}
.field span{flex:1;border-bottom:.6px solid var(--rule);height:6px}
.fax-checks{position:absolute;left:18px;top:208px;width:264px;display:flex;justify-content:space-between;font-size:5px}
.check{display:flex;align-items:center;gap:3px;white-space:nowrap}
.check i{width:6px;height:6px;border:.6px solid var(--ink)}

.envelope-back{left:720px;top:24px;width:456px;height:186px}
.envelope-back .brand{position:absolute;left:50%;top:52px;transform:translateX(-50%);font-size:14px}
.envelope-back .brand-dot{width:15px;height:15px}
.envelope-front{left:720px;top:222px;width:456px;height:180px}
.envelope-front .brand{position:absolute;left:16px;top:18px;font-size:22px}
.envelope-front .brand-dot{width:22px;height:22px}
.envelope-front .contact{left:18px;top:52px;font-size:5.5px}
.envelope-front .web{position:absolute;right:16px;bottom:8px;font-size:5px;color:var(--paper)}

.card{position:absolute;width:132px;height:74px;overflow:hidden;border-radius:2px;box-shadow:0 2px 6px rgba(0,0,0,.5)}
.card-front{left:756px;top:416px;background:var(--paper)}
.card-front .brand{position:absolute;left:10px;top:22px;font-size:9px}
.card-front .brand-dot{width:10px;height:10px}
.card-back{left:924px;top:416px;background:var(--paper)}
.card-back .brand{position:absolute;left:7px;top:12px;font-size:7px}
.card-back .brand-name{width:48px}
.card-back .brand-dot{width:8px;height:8px}
.card-back .person{position:absolute;left:68px;top:9px;width:60px;font-size:4.5px;line-height:6px}
.card-back .person strong{color:var(--red);font-weight:600;font-size:5.5px}
.card-back .contact{left:68px;top:30px;font-size:3.6px;line-height:5.5px}
.card-red{left:756px;top:494px;background:var(--red)}
.card-dark{left:924px;top:494px;background:var(--card-dark)}
.card-red .brand,.card-dark .brand{position:absolute;left:50%;top:50%;transform:translate(-50%,-50%);font-size:9px}
.card-red .brand-dot,.card-dark .brand-dot{width:10px;height:10px}
.card-dark .web{position:absolute;left:0;right:0;bottom:7px;text-align:center;font-size:4.5px;color:var(--muted)}
</style>
</head>
<body>

<section class="sheet letterhead">
  <div class="brand stacked"><span class="brand-dot"></span><span class="brand-name">Bright Path Fund</span></div>
  <div class="contact">20573 Lindale Avenue #238<br>Helotes, Texas 78154<br><b>T:</b> 210.555.0142<br><b>F:</b> 210.555.0143<br>dale.meridew@brightpathfund.org<br><b>www.brightpathfund.org</b></div>
  <svg class="swoosh" viewBox="0 0 300 80" height="80" preserveAspectRatio="none">
    <path d="M0 36 Q150 -6 300 30 L300 80 L0 80Z" fill="var(--red)"/>
    <path d="M0 30 Q150 -14 300 22 L300 30 Q150 -4 0 42Z" fill="var(--band-grey)"/>
    <path d="M0 48 Q160 14 300 40 L300 46 Q160 24 0 56Z" fill="var(--paper)"/>
  </svg>
</section>

<section class="sheet fax">
  <div class="brand stacked"><span class="brand-dot"></span><span class="brand-name">Bright Path Fund</span></div>
  <div class="contact">20573 Lindale Avenue #238<br>Helotes, Texas 78154<br><b>T:</b> 210.555.0142<br><b>F:</b> 210.555.0143<br>dale.meridew@brightpathfund.org<br><b>www.brightpathfund.org</b></div>
  <h1 class="fax-title">FAX</h1>
  <div class="fax-fields">
    <div class="field">To:<span></span></div><div class="field">From:<span></span></div>
    <div class="field">Fax:<span></span></div><div class="field">Pages:<span></span></div>
    <div class="field">Phone:<span></span></div><div class="field">Date:<span></span></div>
    <div class="field">Re:<span></span></div><div class="field">CC:<span></span></div>
  </div>
  <div class="fax-checks">
    <div class="check"><i></i>Urgent</div>
    <div class="check"><i></i>For Review</div>
    <div class="check"><i></i>Please Comment</div>
    <div class="check"><i></i>Please Reply</div>
    <div class="check"><i></i>Please Recycle</div>
  </div>
  <svg class="swoosh" viewBox="0 0 300 80" height="80" preserveAspectRatio="none">
    <path d="M0 36 Q150 -6 300 30 L300 80 L0 80Z" fill="var(--red)"/>
    <path d="M0 30 Q150 -14 300 22 L300 30 Q150 -4 0 42Z" fill="var(--band-grey)"/>
    <path d="M0 48 Q160 14 300 40 L300 46 Q160 24 0 56Z" fill="var(--paper)"/>
  </svg>
</section>

<section class="sheet envelope-back">
  <svg width="456" height="186" viewBox="0 0 456 186" style="position:absolute;left:0;top:0">
    <path d="M0 0 H456 V40 Q228 70 0 40Z" fill="var(--red)"/>
    <path d="M0 40 L228 120 L456 40" fill="none" stroke="var(--rule)" stroke-width="1"/>
  </svg>
  <div class="brand single"><span class="brand-dot"></span><span class="brand-name">Bright Path Fund</span></div>
</section>

<section class="sheet envelope-front">
  <div class="brand single"><span class="brand-dot"></span><span class="brand-name">Bright Path Fund</span></div>
  <div class="contact">20573 Lindale Avenue #238, Helotes, Texas 78154</div>
  <svg class="swoosh" viewBox="0 0 456 40" height="40" preserveAspectRatio="none">
    <path d="M0 22 Q228 -4 456 18 L456 40 L0 40Z" fill="var(--red)"/>
    <path d="M0 18 Q228 -10 456 12 L456 16 Q228 -4 0 24Z" fill="var(--band-grey)"/>
  </svg>
  <div class="web">www.brightpathfund.org</div>
</section>

<section class="card card-front">
  <div class="brand single"><span class="brand-dot"></span><span class="brand-name">Bright Path Fund</span></div>
  <svg class="swoosh" viewBox="0 0 132 16" height="16" preserveAspectRatio="none">
    <path d="M0 8 Q66 -2 132 6 L132 16 L0 16Z" fill="var(--red)"/>
  </svg>
</section>

<section class="card card-back">
  <div class="brand stacked"><span class="brand-dot"></span><span class="brand-name">Bright Path Fund</span></div>
  <div class="person"><strong>Dale Meridew</strong><br>President and Chairman of the Board</div>
  <div class="contact">20573 Lindale Avenue #238<br>Helotes, Texas 78154<br>dale.meridew@brightpathfund.org<br>www.brightpathfund.org</div>
  <svg class="swoosh" viewBox="0 0 132 12" height="12" preserveAspectRatio="none">
    <path d="M0 6 Q66 -2 132 5 L132 12 L0 12Z" fill="var(--red)"/>
  </svg>
</section>

<section class="card card-red">
  <div class="brand single on-red"><span class="brand-dot"></span><span class="brand-name">Bright Path Fund</span></div>
</section>

<section class="card card-dark">
  <div class="brand single on-dark"><span class="brand-dot"></span><span class="brand-name">Bright Path Fund</span></div>
  <div class="web">www.brightpathfund.org</div>
</section>

</body>
</html>
```